Half-off Holiday Sale: Tremorwell Academy

The online course called Tremorwell Academy. Once a year, I run a 1/2 off special (expired Dec 31). You can see what the school is all about here: tremorwell-academy.net and I'll attach a picture of the current ad we're running.
www.tremorwell-academy.net

Please stick with the brain/puzzle logo as the theme, but make the 50% off appealing and inviting.

** I plan on paying for more than one design. I'd like to buy a few different ones!

Target Market(s)

People with Parkinson's disease and their families.

Industry/Entity Type

medical care/ education

Requirements
Must have
• TA School (Tremorwell Academy) logo; Must say "50% off" or something like that.

```html
<!DOCTYPE html>
<html lang="en">
<head>
<meta charset="utf-8">
<title>Tremorwell Academy – 50% Off</title>
<link rel="stylesheet" href="https://fonts.googleapis.com/css2?family=Exo+2:wght@600;700&family=Arimo:wght@400&family=Barlow+Condensed:wght@600&display=swap">
<style>
  :root {
    --paper: #efefee;
    --ink-grey: #7a7a7a;
    --tagline-grey: #6a6a6a;
    --frame-grey: #9c9c9c;
    --orange-light: #d9643f;
    --orange-deep: #c8461f;
    --white: #ffffff;
  }
  html, body {
    margin: 0;
    padding: 0;
    width: 1200px;
    height: 1200px;
    overflow: hidden;
    background: var(--paper);
  }
  .sale-card {
    position: relative;
    width: 1200px;
    height: 1200px;
    background: var(--paper);
  }
  .sale-art {
    position: absolute;
    inset: 0;
  }
  .brand-mark { fill: var(--ink-grey); }
  .brand-name {
    font-family: "Exo 2", sans-serif;
    font-weight: 700;
    fill: var(--ink-grey);
  }
  .brand-tagline {
    font-family: "Arimo", sans-serif;
    font-weight: 400;
    fill: var(--tagline-grey);
  }
  .offer-frame {
    fill: none;
    stroke: var(--frame-grey);
    stroke-width: 4;
  }
  .offer-panel-deep { fill: var(--orange-deep); }
  .offer-panel-light { fill: var(--orange-light); }
  .offer-slash { fill: var(--white); }
  .offer-figure, .offer-percent, .offer-off {
    font-family: "Barlow Condensed", sans-serif;
    font-weight: 600;
    fill: var(--white);
  }
  .offer-expiry {
    font-family: "Exo 2", sans-serif;
    font-weight: 600;
    fill: var(--white);
  }
</style>
</head>
<body>
<main class="sale-card">
  <svg class="sale-art" width="1200" height="1200" viewBox="0 0 1200 1200" xmlns="http://www.w3.org/2000/svg">
    <!-- Brand block -->
    <circle class="brand-mark" cx="598" cy="222" r="112"/>
    <text class="brand-name" x="599" y="448" text-anchor="middle" font-size="68" textLength="806" lengthAdjust="spacingAndGlyphs">TREMORWELL ACADEMY</text>
    <text class="brand-tagline" x="599" y="488" text-anchor="middle" font-size="27">An Online Course for Patients and Providers</text>

    <!-- Offer block -->
    <rect class="offer-frame" x="114" y="580" width="971" height="451"/>
    <rect class="offer-panel-deep" x="180" y="640" width="840" height="476"/>
    <polygon class="offer-panel-light" points="180,640 771,640 531,1116 180,1116"/>
    <polygon class="offer-slash" points="746,676 760,676 547,1098 533,1098"/>

    <text class="offer-figure" x="313" y="1040" font-size="440" textLength="330" lengthAdjust="spacingAndGlyphs">50</text>
    <text class="offer-percent" x="690" y="735" font-size="108" textLength="36" lengthAdjust="spacingAndGlyphs">0</text>
    <text class="offer-percent" x="725" y="829" font-size="108" textLength="37" lengthAdjust="spacingAndGlyphs">0</text>
    <text class="offer-off" x="692" y="1004" font-size="178" textLength="196" lengthAdjust="spacingAndGlyphs">OFF</text>
    <text class="offer-expiry" x="754" y="1091" font-size="36" textLength="222" lengthAdjust="spacingAndGlyphs">EXPIRED DEC 31</text>
  </svg>
</main>
</body>
</html>
```